Exciting New Reseller Brand requires Website to WOW New clients to register.

We are a NEW online business called Trade Your Goods.

The Website is a simple concept, it looks to put Merchants (businesses that want their products resold) in touch with Resellers (people or businesses that want to resell that product).

The website acts as an online market place which looks to get Merchants to sign-up and pay to list their company and product as well as getting Resellers to sign-up to view potential Merchants they can get in touch with in the right industry or area to resell their products for (see attached slide-pack to explain packages)

Any type of Industry or Business can register themselves to get listed on Trade Your Goods to see either get their product/service resold or to look for products / services to reseller.

Trade Your Goods does not take any other monetary part in the business relationships other than to obtain money for the monthly website subscription.

We want a very simple website, so this project is for several pages:

Page 1) A really vibrant, exciting, image based homepage to get people to sign-up / register (see sites that we like in the project brief). Needs to be very clear that there are 2 customers and to sign up to join, build and earn!

Page 2) A page that describes the benefits and packages for Resellers.

Page 3) A page that describes the benefits and packages for Merchants.

Page 4) The Payment process pages, taking the customer through sign-up

Page 5) The Business Listings page, so when people search for a Merchant how this will be displayed.

We would really like an image based site and preferably parallax. We want it bright vibrant and to look like a social media site.

All necessary files / logos enclosed.

We would love to continue to work with the winning designer moving forward.

Many thanks and Good Luck.

Regards

Martin & Owen

Target Market(s)

Merchants, Suppliers, Vendors, Manufacturers, Distributors, Wholesalers, Affiliate programs, Franchisees, Reselers

Industry/Entity Type

Business

Number of Pages Required

5+ page

Requirements
Must have
• We love the following websites:
• 1) Like the top section, i.e. parallax image based: www.brightfoxstudio.co.uk
• 2) Like the way the screen is split in 2, could be used to describe the 2 different customers we are after Merchants / Resellers: www.cloudtrunk.example/guide
• 3) Like the bright colours / full screen video split into 2 below top banner and the generally how simple the site is: www.harbourlinden.com.au
• 4) Love all of this site, simple, bold, Love the colours, the clear message and the infographics: http://www.velomiro.example/swiftride/quicker

```html
<!DOCTYPE html>
<html lang="en">
<head>
<meta charset="utf-8">
<title>Trade Your Goods – Virtual Sales Team</title>
<link rel="stylesheet" href="https://fonts.googleapis.com/css2?family=Open+Sans:wght@300;400;600;700;800&display=swap">
<style>
:root{
  --blue:#1a8cd8;
  --green:#82c341;
  --ink:#555b61;
  --muted:#9a9ea3;
  --light:#f1f1f1;
  --dark:#2f3133;
  --white:#ffffff;
  --grey-dot:#6d6e70;
}
*{box-sizing:border-box;margin:0;padding:0}
html,body{width:1200px;height:3689px;overflow:hidden}
body{font-family:"Open Sans",Arial,sans-serif;color:var(--ink);background:var(--white);position:relative}
section,header,footer{position:relative;width:1200px;overflow:hidden}
ul{list-style:none}

/* header */
.site-header{height:93px;background:var(--white);display:flex;align-items:center;padding:0 98px}
.brand{display:flex;align-items:center;gap:12px;font-weight:700;font-size:28px;color:var(--blue)}
.brand-dot{width:34px;height:34px;border-radius:50%;background:var(--green)}
.main-nav{margin-left:auto;display:flex;gap:58px;font-size:13px;text-transform:uppercase;letter-spacing:.5px;color:#444}
.main-nav .active{color:var(--blue)}

/* hero */
.hero{height:627px;background:linear-gradient(160deg,#6b6f73 0%,#4a4d50 45%,#3a3c3e 100%);text-align:center;color:var(--white)}
.hero-text{position:absolute;top:200px;left:0;right:0}
.hero-kicker{font-size:52px;font-weight:400}
.hero-title{font-size:72px;font-weight:700;line-height:1.1}
.hero-tag{font-size:44px;font-weight:600;margin-top:6px}
.hero-arrow{position:absolute;top:370px}
.hero-arrow.left{left:28px}.hero-arrow.right{right:28px}

/* split */
.split{height:365px;display:flex}
.split-video{width:602px;background:linear-gradient(135deg,#a6d54a,#84c23c);position:relative}
.play{position:absolute;left:235px;top:120px;width:130px;height:130px;border:3px solid var(--white);border-radius:50%;color:var(--white);font-size:22px;font-weight:600;display:flex;align-items:center;justify-content:center;text-align:center;line-height:1.2}
.split-offer{flex:1;background:linear-gradient(135deg,#7e6a58,#4e4640);color:var(--white);padding:108px 0 0 70px}
.split-offer h2{font-size:32px;font-weight:600;line-height:1.3}
.btn-outline{display:inline-block;border:2px solid var(--white);color:var(--white);font-size:14px;text-transform:uppercase;padding:11px 20px;margin-top:26px;letter-spacing:.5px}

/* feature rows */
.feature{display:flex;align-items:center}
.feature h2{font-size:36px;font-weight:700;color:#55595e}
.feature .lead{font-size:13px;color:var(--muted);line-height:1.6;margin:18px 0 30px;max-width:420px}
.feature li{font-size:13px;color:#6a6e73;margin-bottom:14px}
.feature li::before{content:"• "}
.what-we-do{height:440px;background:var(--light)}
.what-we-do .media{width:360px;height:300px;margin-left:150px;background:linear-gradient(160deg,#3b3f9e,#7b3fb5 50%,#c9ccd1 80%);border-radius:6px}
.what-we-do .copy{margin-left:170px}
.why-reselling{height:455px;background:var(--white)}
.why-reselling .copy{width:660px;padding-left:98px}
.why-reselling .media{width:540px;height:455px;background:linear-gradient(135deg,#f6f6f5,#d9dcdf 60%,#e9d6c7)}

/* audiences */
.audiences{height:400px;display:flex;color:var(--white);text-align:center}
.audience{width:50%;padding-top:40px}
.audience.merchants{background:var(--blue)}
.audience.resellers{background:var(--green)}
.audience h3{font-size:38px;font-weight:700;margin-top:10px}
.audience .sub{font-size:16px;font-weight:600}
.audience .who{font-size:13px;line-height:1.7;margin-top:18px}
.audience .btn-outline{margin-top:26px}

/* benefits */
.benefits{height:382px;background:var(--white);display:flex;align-items:flex-start;padding:70px 98px 0}
.benefits h2{font-size:36px;font-weight:700;line-height:1.2;color:#55595e}
.benefits ul{margin-top:36px}
.benefits li{font-size:13px;color:#6a6e73;margin-bottom:14px}
.benefit-col{width:360px}
.benefit-col.right{text-align:right;margin-left:auto}
.benefit-col.left li::before{content:"• "}
.benefit-col.right li::after{content:" •"}
.benefit-media{width:300px;height:270px;margin-top:-30px;border-radius:4px;background:linear-gradient(180deg,#ffffff 0%,#e3efd6 35%,#d9cdb0 75%,#ffffff 100%)}

/* how it works */
.how{height:381px;background:var(--light);text-align:center;padding-top:50px}
.how h2{font-size:36px;font-weight:700;color:#55595e}
.how .lead{font-size:13px;color:var(--muted);line-height:1.6;margin:16px auto 0;width:460px}
.flow{display:flex;align-items:center;justify-content:center;margin-top:52px}
.step{width:96px;height:96px;border-radius:50%;display:flex;align-items:center;justify-content:center;font-size:15px;background:var(--white)}
.step.blue-fill{background:var(--blue);color:var(--white)}
.step.blue-ring{border:2px solid var(--blue);color:var(--ink)}
.step.green-ring{border:2px solid var(--green);color:var(--ink)}
.step.green-fill{background:var(--green);color:var(--white)}
.step.hub{width:118px;height:118px;background:var(--grey-dot);color:var(--white);font-weight:700;font-size:15px;line-height:1.2;text-transform:uppercase}
.flow svg{margin:0 12px}

/* contact */
.contact{height:462px;display:flex}
.contact-map{width:602px;background:linear-gradient(135deg,#e4e4e4,#cfcfcf)}
.contact-panel{flex:1;background:var(--blue);color:var(--white);padding:36px 0 0 64px}
.contact-panel h2{font-size:36px;font-weight:700}
.contact-info{display:flex;gap:70px;font-size:13px;line-height:1.55;margin-top:14px}
.contact-form{display:flex;gap:10px;margin-top:52px}
.fields{display:flex;flex-direction:column;gap:10px}
.field{width:160px;height:46px;border:1px solid rgba(255,255,255,.8);font-size:12px;padding:14px 10px}
.field.message{width:268px;height:156px}
.send{display:inline-block;border:2px solid var(--white);border-radius:26px;padding:12px 38px;font-size:13px;text-transform:uppercase;margin-top:22px}

/* footer */
.site-footer{height:84px;background:var(--dark);display:flex;align-items:center;padding:0 98px;font-size:11px;color:#9b9b9b}
.social{margin-left:auto;display:flex;gap:14px}
.social span{width:22px;height:22px;display:block}
</style>
</head>
<body>

<header class="site-header">
  <div class="brand"><span class="brand-dot"></span>Trade Your Goods</div>
  <nav class="main-nav">
    <span class="active">Home</span><span>About Us</span><span>Services</span><span>Our Work</span><span>Products</span><span>Contact</span>
  </nav>
</header>

<section class="hero" role="img" aria-label="Photograph of business people signing documents at a desk">
  <svg class="hero-arrow left" width="28" height="80" viewBox="0 0 28 80"><polyline points="26,2 2,40 26,78" fill="none" stroke="#fff" stroke-opacity=".6" stroke-width="2"/></svg>
  <svg class="hero-arrow right" width="28" height="80" viewBox="0 0 28 80"><polyline points="2,2 26,40 2,78" fill="none" stroke="#fff" stroke-opacity=".6" stroke-width="2"/></svg>
  <div class="hero-text">
    <div class="hero-kicker">Building your own</div>
    <div class="hero-title">Virtual Sales Team</div>
    <div class="hero-tag">Join - Build - Earn</div>
  </div>
</section>

<section class="split">
  <div class="split-video" role="img" aria-label="Video still tinted green">
    <div class="play">PLAY<br>VIDEO</div>
  </div>
  <div class="split-offer" role="img" aria-label="Photograph of a business meeting, darkened">
    <h2>Bringing reseller opportunities<br>to the masses.</h2>
    <span class="btn-outline">Sign-up / Register</span>
  </div>
</section>

<section class="feature what-we-do">
  <div class="media" role="img" aria-label="Desktop computer screen showing the website"></div>
  <div class="copy">
    <h2>What We DO!</h2>
    <p class="lead">Lorem ipsum dolor sit amet, consectetur adipiscing elit, sed do eiusmod tempor incididunt ut labore et dolore magna aliqua.</p>
    <ul>
      <li>Portal for Resellers and Merchants.</li>
      <li>Merchants can promote their products.</li>
      <li>Merchants can build a virtual sales team.</li>
      <li>Resellers can expand product portfolio.</li>
      <li>Resellers can generate revenue.</li>
      <li>Industry news and opportunities.</li>
    </ul>
  </div>
</section>

<section class="feature why-reselling">
  <div class="copy">
    <h2>Why Pick Reselling</h2>
    <p class="lead">Lorem ipsum dolor sit amet, consectetur adipiscing elit, sed do eiusmod tempor incididunt ut labore et dolore magna aliqua.</p>
    <ul>
      <li>Personal requirement for a reseller base.</li>
      <li>Experienced reseller models that work.</li>
      <li>Building an effective virtual sales team.</li>
      <li>Helping SME's earn money for old rope.</li>
      <li>Easy to generate revenue for a minimal cost</li>
    </ul>
  </div>
  <div class="media" role="img" aria-label="Photograph of hands typing on a laptop showing the website"></div>
</section>

<section class="audiences">
  <div class="audience merchants">
    <svg width="80" height="80" viewBox="0 0 80 80" fill="none" stroke="#fff" stroke-width="4"><circle cx="34" cy="28" r="14"/><path d="M10 66c2-16 12-22 24-22s22 6 24 22"/><line x1="52" y1="52" x2="70" y2="70"/></svg>
    <h3>Merchants</h3>
    <div class="sub">Grow Business &amp; Increase Sales</div>
    <p class="who">Products, Suppliers, Vendors,Manufacturers,<br>Distributors, Wholesalers, Affiliate programs,Franchise</p>
    <span class="btn-outline">Sign up to join</span>
  </div>
  <div class="audience resellers">
    <svg width="80" height="80" viewBox="0 0 80 80" fill="none" stroke="#fff" stroke-width="4"><circle cx="22" cy="20" r="9"/><circle cx="58" cy="20" r="9"/><path d="M6 56c0-14 6-22 16-22s16 8 16 22"/><path d="M42 56c0-14 6-22 16-22s16 8 16 22"/><path d="M26 66h28"/></svg>
    <h3>Resellers</h3>
    <div class="sub">Grow Business &amp; Increase Sales</div>
    <p class="who">Resellers, Retailers, Dealers, Distributors<br>Referral partners, Wholesalers,Affiliates,Franchisees</p>
    <span class="btn-outline">Build and earn!</span>
  </div>
</section>

<section class="benefits">
  <div class="benefit-col left">
    <h2>Benefits for<br>Merchants</h2>
    <ul>
      <li>Additional Source of Sales</li>
      <li>Incremental Growth</li>
      <li>Viral Brand Recognition</li>
      <li>Virtual Sales Team</li>
      <li>No Overheads</li>
    </ul>
  </div>
  <div class="benefit-media" role="img" aria-label="Photograph of a young plant growing from a pile of coins"></div>
  <div class="benefit-col right">
    <h2>Benefits for<br>Resellers</h2>
    <ul>
      <li>Additional Stream of Income</li>
      <li>Infrastructure in Place</li>
      <li>No Additional Cost</li>
      <li>Expand Product Suite</li>
      <li>Reach New Target Markets</li>
    </ul>
  </div>
</section>

<section class="how">
  <h2>How it Works!</h2>
  <p class="lead">Lorem ipsum dolor sit amet, consectetur adipiscing elit, sed do eiusmod tempor incididunt ut labore et dolore magna aliqua.</p>
  <div class="flow">
    <div class="step blue-fill">Merchants</div>
    <svg width="30" height="20" viewBox="0 0 30 20"><path d="M0 6h18V0l12 10-12 10v-6H0z" fill="#d0d0d0"/></svg>
    <div class="step blue-ring">Payment</div>
    <svg width="30" height="20" viewBox="0 0 30 20"><path d="M0 6h18V0l12 10-12 10v-6H0z" fill="#d0d0d0"/></svg>
    <div class="step blue-ring">Listing</div>
    <svg width="30" height="20" viewBox="0 0 30 20"><path d="M0 6h18V0l12 10-12 10v-6H0z" fill="#d0d0d0"/></svg>
    <div class="step hub">Promote<br>and earn</div>
    <svg width="30" height="20" viewBox="0 0 30 20"><path d="M30 6H12V0L0 10l12 10v-6h18z" fill="#d0d0d0"/></svg>
    <div class="step green-ring">Search</div>
    <svg width="30" height="20" viewBox="0 0 30 20"><path d="M30 6H12V0L0 10l12 10v-6h18z" fill="#d0d0d0"/></svg>
    <div class="step green-ring">Register</div>
    <svg width="30" height="20" viewBox="0 0 30 20"><path d="M30 6H12V0L0 10l12 10v-6h18z" fill="#d0d0d0"/></svg>
    <div class="step green-fill">Resellers</div>
  </div>
</section>

<section class="contact">
  <div class="contact-map" role="img" aria-label="Street map showing the office location"></div>
  <div class="contact-panel">
    <h2>Contact Us</h2>
    <div class="contact-info">
      <p>info@tradeyourgoods.example<br>Our office is located in the Dummy Address<br>Building on Harbour Lane.</p>
      <p><br>Tel: +000 555 0142<br>Sign Up for Newsletter</p>
    </div>
    <div class="contact-form">
      <div class="fields">
        <div class="field">Enter Name</div>
        <div class="field">Email</div>
        <div class="field">Phone</div>
      </div>
      <div class="field message">Message</div>
    </div>
    <span class="send">Send Message</span>
  </div>
</section>

<footer class="site-footer">
  <span>© Copyright 2015 All Rights Reserved. Trade Your Goods</span>
  <div class="social">
    <span style="background:#3b5998"></span><span style="background:#29a9e1"></span><span style="background:#ff0084"></span><span style="background:#d34836"></span><span style="background:#0e76a8"></span><span style="background:#ea4c89"></span><span style="background:#e05a46"></span>
  </div>
</footer>

</body>
</html>
```